Flyer-Design für Wellness Einrichtung mit Kosmetikbereich
Zielgruppe
Wir die 'Weimarer Lichtquelle' sehen uns als Wellness Einrichtung. Bei uns können die Leute entspannen und Energie tanken. Zusätzlich zu unserer Lichtquelle und den Wellness Massagen haben wir nun auch einen Kosmetikbereich. Hier für benötigen wir ein schicken Flyer der unsere Kosmetikangebote inkl. Preisen beinhaltet. Wir nutzen Frische Natur Kosmetik von der Firma Velmora.
Unsere Webseite www.weimarer-lichtquelle-beispiel.de zur Orientierung
Texte im Anhang als doc. Datei (nicht final)
Aufgabenstellung
Wir wünschen uns ein Faltblatt, gefalzt auf DIN lang hoch und 4-seitig. Naturfarben wie grün, beige oder braun würden uns sehr gefallen. Dabei sollten die Farben eher etwas heller dargestellt werden. Im Anhang findet ihr ein paar Bilder, die eventuell genutzt werden können. Auch findet ihr dort alle erforderlichen Texte im Anhang als doc. Datei.
Front-Seite: Logo, unter dem Logo Text dezent Wellness I Kosmetik I Massagen
Dateiformat: jpg und psd

```html
<!DOCTYPE html>
<html lang="de">
<head>
<meta charset="utf-8">
<title>Weimarer Lichtquelle – Flyer</title>
<link rel="stylesheet" href="https://fonts.googleapis.com/css2?family=Roboto:ital,wght@0,700;1,700&display=swap">
<style>
  :root {
    --paper-top: #f4f3f2;
    --paper-mid: #dedcdb;
    --paper-low: #a8a5a4;
    --brand-orange: #e2781c;
    --headline-brown: #3d2f27;
    --partner-box: #7f7b79;
    --partner-edge: #b9b5b3;
    --partner-text: #2a2523;
    --band-tan: #e9b57c;
    --band-brown: #6a4328;
    --photo-dark: #2a1a10;
    --photo-warm: #7a4a26;
    --photo-glow: #c98a3c;
  }
  * { margin: 0; padding: 0; box-sizing: border-box; }
  html, body { width: 1200px; height: 2365px; overflow: hidden; background: #ffffff; }
  .flyer {
    position: relative;
    width: 1200px;
    height: 2365px;
    overflow: hidden;
    font-family: "Roboto", Arial, sans-serif;
    background: linear-gradient(180deg, var(--paper-top) 0%, var(--paper-mid) 30%, var(--paper-low) 64%);
  }
  .brand {
    position: absolute;
    left: 120px;
    top: 150px;
    width: 480px;
    text-align: center;
    color: var(--brand-orange);
    font-weight: 700;
  }
  .brand-dot {
    display: block;
    width: 110px;
    height: 110px;
    margin: 0 auto 18px;
    border-radius: 50%;
    background: var(--brand-orange);
  }
  .brand-city {
    display: block;
    font-size: 30px;
    letter-spacing: 6px;
    text-transform: uppercase;
    line-height: 1;
    margin-bottom: 6px;
  }
  .brand-name {
    display: block;
    font-size: 86px;
    line-height: 1;
  }
  .headline {
    position: absolute;
    left: 0;
    top: 565px;
    width: 1200px;
    text-align: center;
    color: var(--headline-brown);
    font-style: italic;
    font-weight: 700;
    font-size: 112px;
    line-height: 156px;
    letter-spacing: -1px;
  }
  .partner {
    position: absolute;
    left: 332px;
    top: 1185px;
    width: 536px;
    height: 211px;
    border: 3px solid var(--partner-edge);
    border-radius: 8px;
    background: linear-gradient(180deg, #8b8785 0%, var(--partner-box) 100%);
    display: flex;
    align-items: center;
    justify-content: center;
  }
  .partner-name {
    color: var(--partner-text);
    font-weight: 700;
    font-size: 84px;
    letter-spacing: 14px;
    text-transform: uppercase;
  }
  .band-tan {
    position: absolute;
    left: 0; top: 1512px;
    width: 1200px; height: 30px;
    background: linear-gradient(90deg, var(--band-tan), #f3cc9c 50%, var(--band-tan));
  }
  .band-brown {
    position: absolute;
    left: 0; top: 1542px;
    width: 1200px; height: 24px;
    background: var(--band-brown);
  }
  .gap {
    position: absolute;
    left: 0; top: 1566px;
    width: 1200px; height: 14px;
    background: #f1eeec;
  }
  .spa-photo {
    position: absolute;
    left: 0; top: 1580px;
    width: 1200px; height: 785px;
    background:
      radial-gradient(ellipse 260px 200px at 500px 260px, rgba(232, 190, 40, 0.55), transparent 70%),
      radial-gradient(ellipse 300px 180px at 900px 380px, rgba(240, 220, 170, 0.45), transparent 70%),
      radial-gradient(ellipse 500px 260px at 350px 560px, rgba(201, 138, 60, 0.5), transparent 70%),
      linear-gradient(180deg, var(--photo-dark) 0%, var(--photo-warm) 60%, var(--photo-dark) 100%);
  }
</style>
</head>
<body>
  <main class="flyer">
    <div class="brand">
      <span class="brand-dot"></span>
      <span class="brand-city">Weimarer</span>
      <span class="brand-name">Lichtquelle</span>
    </div>

    <h1 class="headline">Lassen Sie Ihre<br>Haut mit Natur<br>erstrahlen</h1>

    <div class="partner">
      <span class="partner-name">Velmora</span>
    </div>

    <div class="band-tan"></div>
    <div class="band-brown"></div>
    <div class="gap"></div>

    <div class="spa-photo" role="img" aria-label="Wellness-Stillleben auf dunklem Holz: gerollte Handtücher, gelbe Blume, Kerzen, Seifenstücke, Salz und Massagesteine"></div>
  </main>
</body>
</html>
```